Large multi-office optometry business opening a Dry Eye Spa and needs sign.

Business name/sign info: Brenwick Dry Eye Institute, (555) 362-4817
Backlit pole sign at office entrance on a very busy street
Sign dimensions: 53" tall x 136.5" wide
State of the art Dry Eye Spa for treatment of all forms of dry eye and ocular surface disease. Also, have aesthetics treatments (IPL, Low Level Light Treatment, etc.)

Target Market(s)

People who are suffering from: dryness, burning, foreign body sensation, itching, fluctuating vision, tired eyes, etc.

Industry/Entity Type

Optometry and aesthetics

Colors
0054AA
0677BA
7BADD7
CADEEF
E8F1F8

Requirements
Must have
• Business name, phone number, subliminal message of relief in a glance or short look.
Nice to have
• Cool, relief, soothing sense.
Should not have
• Too much information or too busy.

```html
<!DOCTYPE html>
<html lang="en">
<head>
<meta charset="utf-8">
<title>Brenwick Dry Eye Institute – Pole Sign</title>
<link rel="stylesheet" href="https://fonts.googleapis.com/css2?family=Anton&family=Montserrat:wght@800&display=swap">
<style>
  :root {
    --navy: #0a1f82;
    --navy-top: #0c2a9a;
    --blue-deep: #0054AA;
    --blue: #0677BA;
    --blue-bright: #0a80c6;
    --blue-soft: #7BADD7;
    --blue-pale: #CADEEF;
    --blue-mist: #E8F1F8;
    --white: #ffffff;
    --backdrop: #eef1f4;
  }
  * { margin: 0; padding: 0; box-sizing: border-box; }
  html, body {
    width: 1200px;
    height: 904px;
    overflow: hidden;
    background: var(--backdrop);
  }
  .canvas {
    position: relative;
    width: 1200px;
    height: 904px;
    display: flex;
    align-items: center;
    justify-content: center;
  }
  .sign {
    position: relative;
    width: 1120px;
    height: 435px;
    overflow: hidden;
    background: var(--blue-deep);
    box-shadow: 0 12px 30px rgba(0, 30, 80, 0.25);
  }
  .sign__texture {
    position: absolute;
    inset: 0 0 122px 0;
    background:
      radial-gradient(ellipse at 15% 35%, rgba(202, 222, 239, 0.14) 0%, rgba(202, 222, 239, 0) 40%),
      radial-gradient(ellipse at 90% 30%, rgba(202, 222, 239, 0.12) 0%, rgba(202, 222, 239, 0) 35%),
      linear-gradient(172deg, var(--blue-bright) 0%, var(--blue) 45%, var(--blue-deep) 100%);
  }
  .sign__drop-art {
    position: absolute;
    right: 10px;
    top: 40px;
    width: 240px;
    height: 300px;
    background: radial-gradient(closest-side, rgba(123, 173, 215, 0.45) 0%, rgba(6, 119, 186, 0.18) 60%, rgba(6, 119, 186, 0) 100%);
  }
  .sign__name {
    font-family: "Anton", "Impact", sans-serif;
    font-weight: 400;
    color: var(--white);
    text-transform: uppercase;
  }
  .sign__name-top,
  .sign__name-main {
    position: absolute;
    left: 0;
    right: 0;
    text-align: center;
    line-height: 1;
    white-space: nowrap;
    z-index: 3;
  }
  .sign__name-top {
    top: 58px;
    font-size: 115px;
    letter-spacing: 6px;
    transform: translateX(28px) scaleX(1.15);
  }
  .sign__name-main {
    top: 178px;
    font-size: 124px;
    letter-spacing: 1px;
    transform: scaleX(1.13);
  }
  .sign__band {
    position: absolute;
    left: 0;
    bottom: 0;
    width: 100%;
    height: 122px;
    background: linear-gradient(180deg, var(--navy-top) 0%, var(--navy) 100%);
    display: flex;
    align-items: center;
    justify-content: center;
    z-index: 2;
  }
  .sign__phone {
    font-family: "Montserrat", "Arial Black", sans-serif;
    font-weight: 800;
    font-size: 90px;
    line-height: 1;
    color: var(--white);
    letter-spacing: 1px;
    white-space: nowrap;
    padding-top: 8px;
  }
</style>
</head>
<body>
  <main class="canvas">
    <section class="sign" aria-label="Brenwick Dry Eye Institute pole sign">
      <div class="sign__texture" role="img" aria-label="Cool blue field covered in small water droplets"></div>
      <div class="sign__drop-art" role="img" aria-label="Illustration of a single falling water drop landing in rippling water"></div>
      <h1 class="sign__name">
        <span class="sign__name-top">Brenwick</span>
        <span class="sign__name-main">Dry Eye Institute</span>
      </h1>
      <div class="sign__band">
        <p class="sign__phone">CALL: (555) 362-4817</p>
      </div>
    </section>
  </main>
</body>
</html>
```